specialised legal consultancy business needs an update on logo and office stationary.

Update on Logo - see attached.

update on email signature - something new and fresh with only the following details -

(the logo)
Advocate Karel Steenkamp
KS Venture Frameworks (Pty) Ltd (Reg No.: 2019 / 374915 / 07)
LLB, LLM (Cum Laude), Cert.Dir (ABNQE), FCG (PTVRO)
+27 82 596 1174
karel#veldanvik.com

Update on letterhead - something new and fresh and please more user-friendly. With the same details as per the email signature.

```html
<!DOCTYPE html>
<html lang="en">
<head>
<meta charset="utf-8">
<title>KS Venture – Letterhead</title>
<link rel="stylesheet" href="https://fonts.googleapis.com/css2?family=Poppins:wght@400;500;600;700&display=swap">
<style>
  :root {
    --ink: #111111;
    --text: #2a2a2a;
    --muted: #555555;
    --rule: #9a9a9a;
    --band-grey: #b9babd;
    --sign-fill: #ececec;
    --paper: #ffffff;
    --backdrop: #efefee;
  }
  * { box-sizing: border-box; margin: 0; padding: 0; }
  html, body {
    width: 1200px; height: 1200px; overflow: hidden;
    background: var(--backdrop);
    font-family: 'Poppins', sans-serif;
    color: var(--text);
  }
  .letterhead {
    position: absolute; left: 202px; top: 37px;
    width: 796px; height: 1125px;
    background: var(--paper);
    overflow: hidden;
  }
  .brand {
    position: absolute; left: 45px; top: 150px;
    display: flex; align-items: center; gap: 10px;
  }
  .brand-mark { width: 14px; height: 14px; background: var(--ink); }
  .brand-name {
    font-weight: 600; font-size: 22px; letter-spacing: 2px; color: var(--ink);
  }
  .sender { position: absolute; left: 576px; top: 26px; }
  .sender-title { font-size: 11px; font-weight: 500; color: var(--ink); }
  .sender-name { font-size: 23px; font-weight: 600; color: var(--ink); line-height: 1.2; margin-top: 2px; }
  .contact-list { list-style: none; margin-top: 18px; }
  .contact-list li {
    position: relative; padding-left: 29px;
    font-size: 11.5px; line-height: 18px; color: var(--muted); margin-bottom: 5px;
  }
  .contact-list svg { position: absolute; left: 0; top: 3px; width: 13px; height: 13px; fill: var(--ink); }
  .salutation {
    position: absolute; left: 45px; top: 258px;
    font-size: 16px; font-weight: 600; color: var(--ink); letter-spacing: 0.3px;
  }
  .letter-body { position: absolute; left: 45px; top: 334px; width: 712px; }
  .letter-body p { font-size: 14px; line-height: 18.7px; margin-bottom: 18.7px; }
  .letter-body p.joined { margin-bottom: 0; }
  .letter-body p.spaced { margin-bottom: 37px; }
  .signature { position: absolute; left: 45px; top: 786px; width: 186px; }
  .signature-script { width: 170px; height: 48px; margin-left: 12px; background: var(--sign-fill); border-radius: 4px; }
  .signature-rule { height: 1px; background: var(--rule); margin-top: 15px; }
  .signature-label {
    text-align: center; font-size: 11.5px; letter-spacing: 8px; color: var(--muted);
    font-weight: 500; margin-top: 10px;
  }
  .footer-credentials {
    position: absolute; left: 0; right: 0; top: 1041px;
    text-align: center; font-size: 11px; line-height: 19px; color: var(--text);
  }
  .footer-credentials strong { font-weight: 600; color: var(--ink); }
  .footer-bands { position: absolute; left: 0; bottom: 0; width: 796px; height: 35px; }
</style>
</head>
<body>
  <main class="letterhead">
    <div class="brand">
      <span class="brand-mark"></span>
      <span class="brand-name">KS VENTURE</span>
    </div>

    <div class="sender">
      <p class="sender-title">Advocate</p>
      <p class="sender-name">Karel Steenkamp</p>
      <ul class="contact-list">
        <li><svg viewBox="0 0 24 24"><path d="M6.6 10.8a15.1 15.1 0 0 0 6.6 6.6l2.2-2.2a1 1 0 0 1 1-.25 11.4 11.4 0 0 0 3.6.57 1 1 0 0 1 1 1V20a1 1 0 0 1-1 1A17 17 0 0 1 3 4a1 1 0 0 1 1-1h3.5a1 1 0 0 1 1 1c0 1.25.2 2.45.57 3.57a1 1 0 0 1-.25 1z"/></svg>+27 82 596 1174</li>
        <li><svg viewBox="0 0 24 24"><path d="M2 5h20v2l-10 6L2 7z M2 9.3l10 6 10-6V19H2z"/></svg>karel@veldanvik.com</li>
        <li><svg viewBox="0 0 24 24"><path d="M12 2a7 7 0 0 0-7 7c0 5.2 7 13 7 13s7-7.8 7-13a7 7 0 0 0-7-7zm0 9.5A2.5 2.5 0 1 1 12 6.5a2.5 2.5 0 0 1 0 5z"/></svg>214 Bosveld Lane,<br>Waterkloofrand, Pretoria</li>
      </ul>
    </div>

    <h1 class="salutation">To whom it may concern</h1>

    <section class="letter-body">
      <p>Lorem ipsum dolor sit amet, consectetuer adipiscing elit, sed diam nonummy nibh euismod tincidunt ut laoreet dolore magna aliquam erat volutpat.&nbsp; dignissim qui blandit praesent luptatum zzril delenit augue duis dolore te feugait nulla facilisi.</p>
      <p class="joined">Lorem ipsum dolor sit amet, cons ectetuer adipiscing elit, sed diam nonummy nibh euismod tincidunt ut laoreet dolore magna aliquam erat volutpat. Ut wisi enim ad minim veniam, quis nostrud exerci tation ullamcorper suscipit lobortis nisl ut aliquip ex ea commodo consequat.</p>
      <p class="spaced">Lorem ipsum dolor sit amet, consectetuer adipiscing elit, sed diam nonummy nibh euismod tincidunt ut laoreet dolore magna aliquam erat volutpat. Ut wisi enim ad minim veniam, quis nostrud exerci tation ullamcorper suscipit lobortis nisl ut aliquip ex ea commodo consequat.</p>
      <p>Lorem ipsum dolor sit amet, cons ectetuer adipiscing elit, sed diam nonummy nibh euismod tincidunt ut laoreet dolore magna aliquam erat volutpat. Ut wisi enim ad minim veniam, quis nostrud exerci tation ullamcorper suscipit lobortis nisl ut aliquip ex ea commodo consequat.</p>
      <p>Lorem ipsum dolor sit amet vel illum dolore eu feugiat nulla facilisis at vero eros et accumsan et iusto odio dignissim qui blandit praesent luptatum zzril delenit augue duis dolore te feugait nulla facilisi. exerci tation ullamcorper suscipit lobortis nisl ut aliquip ex ea commodo consequat.</p>
    </section>

    <div class="signature">
      <div class="signature-script" role="img" aria-label="Handwritten signature of Karel Steenkamp"></div>
      <div class="signature-rule"></div>
      <p class="signature-label">SIGNATURE</p>
    </div>

    <footer class="footer-credentials">
      <p><strong>KS Venture Frameworks (Pty) Ltd</strong> (Reg No.: 2019 / 374915 / 07) <strong>LLB, LLM</strong> (Cum Laude), <strong>Cert.Dir</strong> (ABNQE), <strong>FCG</strong> (PTVRO)</p>
      <p>Advocate of High Court&nbsp; | &nbsp;Mediator&nbsp; | &nbsp;Chartered Secretary (PTVRO) Nov, 2021&nbsp; | &nbsp;Member of Legal Advisers Guild of South Africa</p>
    </footer>

    <svg class="footer-bands" viewBox="0 0 796 35" aria-hidden="true">
      <polygon points="0,0 588,0 586,5 0,5" fill="var(--ink)"/>
      <polygon points="0,10 583,10 576,35 0,35" fill="var(--ink)"/>
      <polygon points="600,0 796,0 796,5 598,5" fill="var(--band-grey)"/>
      <polygon points="596,10 796,10 796,35 589,35" fill="var(--band-grey)"/>
    </svg>
  </main>
</body>
</html>
```